Company brochure for our unique consulting business

We are a small consulting business offering a unique set of services to our clients.. In simple terms we are a business improvement consultancy helping our clients get the best out of their businesses. We work with clients across multiple sectors and deliver a variety of services. We want to put together a brochure to cover these main themes:1. Who we are2. What we do3. The type of people we employ4. The sectors we work inWhile the brochure needs to have a certain corporate feel to it, we don't want it to be "boring" or "stiff". We would like it to have a slightly "friendly" or "informal" feel to it, to reflect the type of organisation we are.We have a company website http://tollandvergeadvisory.com , however we do not want to directly replicate the content or feel as we recognise it needs updating.We would like the brochure to be A4 portrait format. We anticipate requiring 12 sides (including covers) but we are happy to be guided on this based on the content we have provided.The attached ppt file gives the detail of the content to be included and also shows the proposed pagination. For the front cover we would like to try 2 versions, one with the TVA logo and one with the Tolland Verge Advisory logo (a file of both is attached)One of the most important pages will be the "Our Services" page. We would like this to cover the centre fold. In the ppt file we have shown an example layout, but this is where we need most help - we are clearly not graphic designers! This page will be the most used page in sales meetings etc.Also attached is the following:1. file for our TollandVerge Advisory company logo.2. File for our TVA company logo3. Files for Derek's signatures (for under photos) - Owen's to follow4. Photo of Derek & Owen (person in purple shirt to be cropped out)Thank you and really excited to see what everyone comes back with.Derek & Owen

Target Market(s)

Very broad - Manufacturing, Healthcare, Hospitality

Industry/Entity Type

Management Consulting

Font styles to use
Other font styles liked:
• We use Swiss721, but happy to be guided by designer

Colors
3276b5
85abd2
0355a3
333333
5c5c5c
9d9d9d
d9d9d9

Requirements
Must have
• Corporate feel
Nice to have
• Slightly friendly feel
• Our standard "blue" is (CORRECTION) - R55 G96 B146 #376092 and our standard grey is R197 G178, B179 - #B3B2B2, which we would like to keep, but other colours we are happy to be guided on. Brand guidelines attached.

```html
<!DOCTYPE html>
<html lang="en">
<head>
<meta charset="utf-8">
<title>Tolland Verge Advisory – Brochure Covers</title>
<link rel="stylesheet" href="https://fonts.googleapis.com/css2?family=Lato:wght@400;700&display=swap">
<style>
  :root {
    --backdrop: #2a2a2b;
    --brand-blue: #376092;
    --mid-blue: #4a67a0;
    --soft-blue: #7488b8;
    --pale-blue: #8fa3cc;
    --photo-tint: #5e72a8;
    --flap-black: #141416;
    --paper: #f6f7fb;
    --ink: #1d1d1f;
    --white: #ffffff;
  }
  * { margin: 0; padding: 0; box-sizing: border-box; }
  html, body {
    width: 1200px; height: 789px; overflow: hidden;
    background: var(--backdrop);
    font-family: "Lato", Arial, sans-serif;
  }
  .spread {
    position: absolute; left: 105px; top: 44px;
    width: 990px; height: 700px;
    display: flex;
  }
  .page { position: relative; width: 495px; height: 700px; overflow: hidden; }
  .page svg.art { position: absolute; inset: 0; width: 100%; height: 100%; }

  .back-cover { background: var(--photo-tint); }
  .address {
    position: absolute; left: 40px; bottom: 70px;
    color: var(--white); font-weight: 700; font-size: 15px; line-height: 1.28;
    font-style: normal;
  }
  .address .tel { display: block; margin-top: 18px; }

  .front-cover { background: var(--paper); }
  .wordmark {
    position: absolute; left: 52px; top: 112px;
    display: flex; align-items: center; gap: 8px;
    color: var(--ink); font-weight: 700; font-size: 22px; line-height: 1.05;
  }
  .wordmark .mark-square { width: 12px; height: 12px; background: var(--brand-blue); }

  .flap-url {
    position: absolute; color: var(--white);
    font-size: 11px; letter-spacing: .2px; white-space: nowrap;
    transform-origin: left center;
  }
  .back-cover .flap-url { left: 318px; top: 668px; transform: rotate(-53deg); font-size: 12px; }
  .front-cover .flap-url { left: 40px; top: 520px; transform: rotate(24deg); }
</style>
</head>
<body>
<main class="spread">
  <section class="page back-cover">
    <svg class="art" viewBox="0 0 495 700" preserveAspectRatio="none">
      <defs>
        <linearGradient id="backPhotoTone" x1="0" y1="0" x2="1" y2="1">
          <stop offset="0" stop-color="#6a7db1"/>
          <stop offset="0.55" stop-color="#5b70a7"/>
          <stop offset="1" stop-color="#5469a0"/>
        </linearGradient>
      </defs>
      <rect width="495" height="700" fill="url(#backPhotoTone)" role="img"
            aria-label="Blue-tinted photo of a hand touching a floating business chart"/>
      <polygon class="flap" points="495,440 495,700 300,700" fill="var(--flap-black)"/>
    </svg>
    <address class="address">
      Millbank House<br>
      Canal Row<br>
      Ashford<br>
      TN24 8QP<br>
      United Kingdom
      <span class="tel">Tel: +44 (0)1233 550172</span>
    </address>
    <span class="flap-url">www.tollandvergeadvisory.com</span>
  </section>

  <section class="page front-cover">
    <svg class="art" viewBox="0 0 495 700" preserveAspectRatio="none">
      <defs>
        <linearGradient id="frontPhotoTone" x1="0" y1="0" x2="1" y2="1">
          <stop offset="0" stop-color="#d8dff0"/>
          <stop offset="0.45" stop-color="#4c64a0"/>
          <stop offset="1" stop-color="#c9d3ea"/>
        </linearGradient>
      </defs>
      <polygon class="top-wedge" points="175,0 495,0 495,40 345,62" fill="var(--soft-blue)"/>
      <polygon class="blue-stripe" points="400,20 440,20 200,400 160,380" fill="var(--mid-blue)"/>
      <polygon class="photo" points="455,40 495,40 495,610 430,600 210,430"
               fill="url(#frontPhotoTone)" role="img"
               aria-label="Photo of a businessman in a suit and striped tie using a tablet"/>
      <polygon class="flap" points="0,440 330,585 0,700" fill="var(--flap-black)"/>
    </svg>
    <div class="wordmark">
      <span>Tolland Verge<br>Advisory</span>
      <span class="mark-square"></span>
    </div>
    <span class="flap-url">www.tollandvergeadvisory.com</span>
  </section>
</main>
</body>
</html>
```